Power point for business plan needed for an adult entertainment app and website

Power point / catalogue/ business plan

Will be sent via pdf as a catalog and presented in tv screens via power point.
Should be very sexual and sexy.
The app colours are purple and dark pinks. Check logo below.
The information is in the pdf attached below.

Target Market(s)

Investors who like to invest in apps and online businesses.

Industry/Entity Type

dating app

Font styles to use
Serif
Decorative
Script

Colors
A7469A
B969AE
D3A5CF
EDDBEB
F8F0F9
6B429C
8869AF
B7A5CE
E3DAEB
F3F0F8

Requirements
Must have
• Sleek modern design with pictures that match the information.
Nice to have
• Capable of turning into a catalog or magazine style for display
Should not have
• Slides should not be word heavy.

```html
<!DOCTYPE html>
<html lang="en">
<head>
<meta charset="utf-8">
<title>Management Team</title>
<link rel="stylesheet" href="https://fonts.googleapis.com/css2?family=Noto+Serif&family=Carlito&display=swap">
<style>
  :root {
    --bg: #000000;
    --panel: #0a0a0a;
    --brush: #0c0b0c;
    --rose: #b9609f;
    --orchid: #B969AE;
    --lilac: #D3A5CF;
    --violet: #8869AF;
    --plum: #6B429C;
    --body-text: #dcdcdc;
  }
  html, body {
    margin: 0;
    padding: 0;
    width: 1200px;
    height: 675px;
    overflow: hidden;
    background: var(--bg);
  }
  .slide {
    position: relative;
    width: 1200px;
    height: 675px;
    background: var(--bg);
    overflow: hidden;
  }
  .brush-shapes {
    position: absolute;
    left: 0;
    top: 0;
  }
  .slide-title {
    position: absolute;
    top: 44px;
    left: 0;
    width: 100%;
    margin: 0;
    text-align: center;
    font-family: "Noto Serif", serif;
    font-weight: 400;
    font-size: 41px;
    color: var(--rose);
  }
  .team-member {
    position: absolute;
    top: 200px;
    width: 240px;
    margin-left: -120px;
    text-align: center;
  }
  .portrait {
    width: 158px;
    height: 158px;
    margin: 0 auto;
    border-radius: 50%;
    border: 3px solid var(--violet);
    background: radial-gradient(circle at 50% 40%, #d9cbc2 0%, #a98f80 45%, #e8e6e6 100%);
  }
  .member-name {
    margin: 24px 0 0;
    font-family: "Noto Serif", serif;
    font-size: 19px;
    font-weight: 400;
    color: var(--rose);
  }
  .social-links {
    display: flex;
    justify-content: center;
    gap: 14px;
    margin-top: 20px;
  }
  .social-link {
    width: 23px;
    height: 23px;
    border-radius: 6px;
    background: var(--lilac);
  }
  .team-summary {
    position: absolute;
    top: 494px;
    left: 105px;
    width: 990px;
    margin: 0;
    text-align: center;
    font-family: "Carlito", sans-serif;
    font-size: 17px;
    line-height: 22.5px;
    color: var(--body-text);
  }
  .colour-strip {
    position: absolute;
    left: 0;
    bottom: 0;
    width: 100%;
    height: 11px;
    display: flex;
  }
  .colour-strip span { flex: 1; }
</style>
</head>
<body>
<main class="slide">
  <svg class="brush-shapes" width="1200" height="675" viewBox="0 0 1200 675" aria-hidden="true">
    <path d="M335 52 Q330 66 350 70 L420 70 Q410 98 440 110 Q600 125 760 118 Q840 112 866 98 Q870 72 838 62 Q820 44 760 46 Q640 40 560 36 Q460 30 420 42 Q360 46 335 52 Z" fill="var(--brush)"/>
    <rect x="215" y="188" width="755" height="182" fill="var(--panel)"/>
    <rect x="172" y="448" width="853" height="8" rx="3" fill="#0d0d0d"/>
    <path d="M80 482 Q120 470 300 472 Q600 466 900 468 Q1080 462 1110 478 Q1128 520 1116 574 Q1108 612 1040 620 Q700 634 360 628 Q140 624 84 604 Q58 560 64 516 Q66 492 80 482 Z" fill="var(--brush)"/>
  </svg>

  <h1 class="slide-title">Management Team</h1>

  <section class="team-member" style="left:335px">
    <div class="portrait" role="img" aria-label="Portrait photo of Mrs. Oliver Doe"></div>
    <h2 class="member-name">Mrs. Oliver Doe</h2>
    <div class="social-links">
      <span class="social-link" role="img" aria-label="Social profile 1"></span>
      <span class="social-link" role="img" aria-label="Social profile 2"></span>
      <span class="social-link" role="img" aria-label="Social profile 3"></span>
    </div>
  </section>

  <section class="team-member" style="left:597px">
    <div class="portrait" role="img" aria-label="Portrait photo of Mr. John Doe"></div>
    <h2 class="member-name">Mr. John Doe</h2>
    <div class="social-links">
      <span class="social-link" role="img" aria-label="Social profile 1"></span>
      <span class="social-link" role="img" aria-label="Social profile 2"></span>
      <span class="social-link" role="img" aria-label="Social profile 3"></span>
    </div>
  </section>

  <section class="team-member" style="left:858px">
    <div class="portrait" role="img" aria-label="Portrait photo of Mrs. Bella Doe"></div>
    <h2 class="member-name">Mrs. Bella Doe</h2>
    <div class="social-links">
      <span class="social-link" role="img" aria-label="Social profile 1"></span>
      <span class="social-link" role="img" aria-label="Social profile 2"></span>
      <span class="social-link" role="img" aria-label="Social profile 3"></span>
    </div>
  </section>

  <p class="team-summary">The Company was founded with a group that have a combined 50 years of experience in business development. The teams diverse expertise across many different industries, has helped them become master dynamic client acquisition Through his expertise, he will be able to bring the operations of the business to profitability within its first year of operations. As an owner of a strip bar he has faced hardship in trying to find a platform to employ girls and relied on word of mouth.</p>

  <div class="colour-strip" aria-hidden="true">
    <span style="background:var(--orchid)"></span>
    <span style="background:var(--lilac)"></span>
    <span style="background:var(--violet)"></span>
    <span style="background:var(--plum)"></span>
    <span style="background:var(--orchid)"></span>
  </div>
</main>
</body>
</html>
```